VS Business Card

Design new business cards for VELNAstack

Please see attached for the design brief

**** Please note, please feel free to propose a font that works for a professional, technology company ***

Target Market(s)

Technology buyers

Industry/Entity Type

Business

```html
<!DOCTYPE html>
<html lang="en">
<head>
<meta charset="utf-8">
<title>VELNAstack Business Card</title>
<link rel="stylesheet" href="https://fonts.googleapis.com/css2?family=Federo&family=Ubuntu:wght@400;500&display=swap">
<style>
  :root {
    --frame-blue: #4a72c0;
    --frame-orange: #f5a42a;
    --frame-green: #0f6b5a;
    --frame-purple: #5a4aa8;
    --card-dark: #051620;
    --card-light: #ffffff;
    --ink-light: #ffffff;
    --ink-navy: #1b2a5e;
    --brand-navy: #16276a;
  }
  * { margin: 0; padding: 0; box-sizing: border-box; }
  html, body {
    width: 1200px;
    height: 720px;
    overflow: hidden;
  }
  body {
    position: relative;
    background: linear-gradient(160deg, var(--frame-blue) 0%, var(--frame-blue) 25%, var(--frame-orange) 55%, var(--frame-green) 80%, var(--frame-purple) 100%);
  }
  .card {
    position: absolute;
    left: 20px;
    top: 18px;
    width: 1161px;
    height: 682px;
    box-shadow: 4px 5px 6px rgba(0, 0, 0, 0.55);
    overflow: hidden;
  }
  .card-identity {
    position: absolute;
    left: 0; top: 0;
    width: 100%;
    height: 491px;
    background: var(--card-dark);
    color: var(--ink-light);
    font-family: "Federo", sans-serif;
    text-align: center;
  }
  .holder-name {
    position: absolute;
    left: 0; right: 0;
    top: 192px;
    font-size: 48px;
    line-height: 1;
  }
  .holder-role {
    position: absolute;
    left: 0; right: 0;
    top: 258px;
    font-size: 48px;
    line-height: 1;
  }
  .card-footer {
    position: absolute;
    left: 0; top: 491px;
    width: 100%;
    height: 191px;
    background: var(--card-light);
    font-family: "Ubuntu", sans-serif;
  }
  .brand {
    position: absolute;
    left: 22px;
    top: 56px;
  }
  .brand-name {
    display: block;
    font-size: 56px;
    font-weight: 500;
    color: var(--brand-navy);
    line-height: 1;
  }
  .brand-tagline {
    margin-top: 14px;
    margin-left: 102px;
    font-size: 18px;
    line-height: 1;
    color: var(--brand-navy);
  }
  .contact-list {
    position: absolute;
    left: 662px;
    top: 14px;
    display: grid;
    grid-template-columns: 102px auto;
    font-size: 26px;
    line-height: 32px;
    color: var(--ink-navy);
  }
</style>
</head>
<body>
  <div class="card">
    <section class="card-identity">
      <p class="holder-name">Martin Halvor</p>
      <p class="holder-role">CEO</p>
    </section>
    <section class="card-footer">
      <div class="brand">
        <span class="brand-name">VELNAstack</span>
        <p class="brand-tagline">..shaping smart business</p>
      </div>
      <dl class="contact-list">
        <dt>phone</dt><dd>+41 41 555 0140</dd>
        <dt>direct</dt><dd>+41 41 555 0141</dd>
        <dt>fax</dt><dd>+41 800 0009 318</dd>
        <dt>mobile</dt><dd>+41 78 555 61 27</dd>
        <dt>email</dt><dd>martin.halvor@velnastack-it.com</dd>
      </dl>
    </section>
  </div>
</body>
</html>
```